Civil Engineering Business Card Design

We need a business card design for an Civil Engineering Company located in Naples, Florida. The company name is Morrow Engineering.
What we do:
Site Evaluation
Review existing site conditions and zoning
Evaluation of potential development options
Evaluation of environmental permitting challenges
Prepare alternative master site development or redevelopment plan
Calculate cost and time lines for site development
Address political, environmental, social, and economic impacts of site development
Site Design
Prepare master site development plans
Zoning, rezoning, and zoning amendments for land use changes
Evaluate zoning and environmental permitting challenges
Value engineer alternative land development design and products
Residential Development
Plat development and design
Homeowner association document development
Single family development ranging from affordable housing to large estate projects
Multi family development ranging from duplexes to large scale condominiums
Amenity facilities such as golf courses, parks and clubhouse sites
Commercial Development
Office site and park designs development plans
Industrial site and park development plans
Shopping center site development design
Hospital site design development
Institutional Development
School design development and redevelopment plans
Park design development and enhancement plans
Downtown redevelopment plans for new and existing structures
Theater and park plan development
Parking garage design development
Governmental administration building design
Design Services
Site development
Environmental assessment
Roadway alignment and development
Surface water management
Drainage design
Water distribution system
Fire service analysis
Sewage collection systems
Sewage pump station and force main design
Cable utility conduit layout
Construction details
Construction documents
Technical specifications
Alternative methods and materials analysis
Services During Construction
Development of bid documents
Solicitation and processing of bids
Cost review and analysis
Construction cost estimating
Onsite construction observation
Coordination of field modifications to address unforeseen site conditions
Assess value engineering design and contract work
Review of pay requests and shop drawings
Review of warranties
Development assessment of onsite and offsite mitigation
Verification of construction completion, close out, and certification
Processing final pay requests and turn over
We want a clean design on a white background. We have a current logo but are not happy with it so changes would be greatly appreciated.
Industry/Entity Type
Construction
Contact Information for Business Card
Morrow Engineering
Practical Site Solutions Grounded in Honesty and Field Practice
Leonard Morrow, President
4870 Bellwood Parkway East
Suite 417C
Corral Bend, GA 34102
555-364-1905-Office, 555-490-6172-Mobile
Leo@MorrowEng.example, www.MorrowEng.example

```html
<!DOCTYPE html>
<html lang="en">
<head>
<meta charset="utf-8">
<title>Morrow Engineering – Business Card</title>
<link rel="stylesheet" href="https://fonts.googleapis.com/css2?family=Poppins:wght@300;400;500;600&display=swap">
<style>
  :root {
    --brand-blue: #0a7cff;
    --icon-blue: #2f6fe8;
    --ink: #1c1c1c;
    --paper: #ffffff;
  }
  * { box-sizing: border-box; margin: 0; padding: 0; }
  html, body { width: 1200px; height: 693px; overflow: hidden; background: var(--paper); }
  .card {
    position: relative;
    width: 1200px;
    height: 693px;
    background: var(--paper);
    font-family: "Poppins", sans-serif;
    color: var(--ink);
  }
  .brand-mark {
    position: absolute;
    left: 164px; top: 80px;
    width: 108px; height: 108px;
    background: var(--brand-blue);
  }
  .brand-name {
    position: absolute;
    left: 40px; top: 208px;
    width: 356px;
    text-align: center;
    font-size: 29px;
    font-weight: 600;
    letter-spacing: 0.5px;
    white-space: nowrap;
  }
  .person {
    position: absolute;
    right: 40px; top: 96px;
    text-align: right;
  }
  .person::after {
    content: "";
    position: absolute;
    right: -28px; top: -1px;
    width: 11px; height: 87px;
    background: var(--brand-blue);
  }
  .person-name {
    font-size: 32px;
    font-weight: 500;
    color: var(--brand-blue);
    letter-spacing: 0.8px;
    line-height: 1.2;
    white-space: nowrap;
  }
  .person-title {
    font-size: 30px;
    font-weight: 300;
    line-height: 1.25;
  }
  .contact-list {
    position: absolute;
    left: 36px; top: 336px;
    list-style: none;
  }
  .contact-item {
    display: flex;
    align-items: center;
    height: 56.5px;
    font-size: 33px;
    font-weight: 300;
    white-space: nowrap;
  }
  .contact-icon {
    width: 28px; height: 28px;
    margin-right: 18px;
    fill: var(--icon-blue);
    flex: none;
  }
  .office {
    position: absolute;
    left: 753px; top: 392px;
  }
  .office-name {
    font-size: 29px;
    font-weight: 600;
    line-height: 1.3;
    margin-bottom: 6px;
  }
  .office-address {
    font-style: normal;
    font-size: 25px;
    font-weight: 300;
    line-height: 1.38;
    white-space: nowrap;
  }
  .tagline {
    position: absolute;
    left: 11px; top: 606px;
    width: 1177px; height: 54px;
    background: var(--brand-blue);
    color: var(--paper);
    font-size: 30px;
    font-weight: 300;
    display: flex;
    align-items: center;
    justify-content: center;
    letter-spacing: 0.3px;
    white-space: nowrap;
  }
</style>
</head>
<body>
  <div class="card">
    <div class="brand-mark"></div>
    <div class="brand-name">MORROW ENGINEERING</div>

    <div class="person">
      <div class="person-name">LEONARD MORROW</div>
      <div class="person-title">President</div>
    </div>

    <ul class="contact-list">
      <li class="contact-item">
        <svg class="contact-icon" viewBox="0 0 24 24" aria-hidden="true"><path d="M6.6 10.8a15.1 15.1 0 0 0 6.6 6.6l2.2-2.2c.3-.3.7-.4 1-.2 1.1.4 2.3.6 3.6.6.6 0 1 .4 1 1V20c0 .6-.4 1-1 1A17 17 0 0 1 3 4c0-.6.4-1 1-1h3.5c.6 0 1 .4 1 1 0 1.3.2 2.5.6 3.6.1.3 0 .7-.2 1z"/></svg>
        555-364-1905
      </li>
      <li class="contact-item">
        <svg class="contact-icon" viewBox="0 0 24 24" aria-hidden="true"><path d="M16 1H8a2.5 2.5 0 0 0-2.5 2.5v17A2.5 2.5 0 0 0 8 23h8a2.5 2.5 0 0 0 2.5-2.5v-17A2.5 2.5 0 0 0 16 1zm-4 20.2a1.2 1.2 0 1 1 0-2.4 1.2 1.2 0 0 1 0 2.4zM16.5 18h-9V4h9z"/></svg>
        555-490-6172
      </li>
      <li class="contact-item">
        <svg class="contact-icon" viewBox="0 0 24 24" aria-hidden="true"><path d="M12 2a10 10 0 1 0 0 20 10 10 0 0 0 0-20zm-1 17.9A8 8 0 0 1 4.2 10.2L9 15v1a2 2 0 0 0 2 2zm6.9-2.5A2 2 0 0 0 16 16h-1v-3a1 1 0 0 0-1-1H8v-2h2a1 1 0 0 0 1-1V7h2a2 2 0 0 0 2-2v-.4a8 8 0 0 1 2.9 12.8z"/></svg>
        www.MorrowEng.example
      </li>
      <li class="contact-item">
        <svg class="contact-icon" viewBox="0 0 24 24" aria-hidden="true"><path d="M20 4H4a2 2 0 0 0-2 2v12a2 2 0 0 0 2 2h16a2 2 0 0 0 2-2V6a2 2 0 0 0-2-2zm0 4-8 5-8-5V6l8 5 8-5z"/></svg>
        Leo@MorrowEng.example
      </li>
    </ul>

    <div class="office">
      <div class="office-name">Morrow Engineering</div>
      <address class="office-address">
        4870 Bellwood Parkway East,<br>
        Suite 417C, Corral Bend, GA 30917
      </address>
    </div>

    <div class="tagline">Practical Site Solutions Grounded in Honesty and Field Practice</div>
  </div>
</body>
</html>
```